Wageline Associates Business Card Design

We need a business card designed around our new logo. The business card should be modern in design & should communicate success, confidence, power, sophistication. The target market is young business professionals. This is for a human resource & payroll outsourcing business.

```html
<!DOCTYPE html>
<html lang="en">
<head>
<meta charset="utf-8">
<title>Wageline Associates – Business Card</title>
<link rel="stylesheet" href="https://fonts.googleapis.com/css2?family=Raleway:wght@400;500;700&display=swap">
<style>
  :root {
    --page-bg: #e9e4de;
    --card-bg: #f3f3f3;
    --card-bg-light: #ffffff;
    --navy: #3a414d;
    --red: #e23a4f;
    --red-dark: #a8253a;
    --text-dark: #2f343c;
    --text-body: #3a3f47;
  }
  * { box-sizing: border-box; margin: 0; padding: 0; }
  html, body {
    width: 1200px; height: 1015px; overflow: hidden;
    background: var(--page-bg);
    font-family: "Raleway", Arial, sans-serif;
  }
  .card {
    position: absolute; left: 340px; top: 52px;
    width: 520px; height: 910px;
    background: linear-gradient(180deg, var(--card-bg-light) 0%, var(--card-bg) 100%);
    box-shadow: 0 14px 40px rgba(60, 45, 30, 0.22);
    overflow: hidden;
  }
  .card-header {
    position: absolute; left: 0; top: 0; width: 520px; height: 440px;
    background: linear-gradient(180deg, var(--navy) 0%, var(--navy) 62%, var(--red-dark) 84%, var(--red) 100%);
  }
  .brand {
    position: absolute; left: 0; right: 0; top: 150px;
    text-align: center; color: #ffffff;
    font-weight: 500; font-size: 42px; line-height: 1.15; letter-spacing: 0.5px;
  }
  .holder { position: absolute; left: 0; right: 0; top: 540px; text-align: center; }
  .holder-name {
    font-size: 31px; color: var(--text-dark); font-weight: 400; letter-spacing: 1px;
  }
  .holder-name strong { font-weight: 700; }
  .holder-role { margin-top: 4px; font-size: 20px; color: var(--red); }
  .contacts {
    position: absolute; left: 118px; top: 650px; list-style: none;
  }
  .contact { display: flex; align-items: center; height: 50px; }
  .contact-icon {
    width: 34px; height: 34px; border-radius: 50%; flex: none;
    display: flex; align-items: center; justify-content: center; margin-right: 18px;
  }
  .contact-icon.is-red { background: var(--red); }
  .contact-icon.is-navy { background: var(--navy); }
  .contact-icon svg { width: 18px; height: 18px; fill: #ffffff; }
  .contact-text { font-size: 17px; color: var(--text-body); line-height: 1.25; font-family: Arial, Helvetica, sans-serif; }
</style>
</head>
<body>
  <article class="card">
    <div class="card-header" role="img" aria-label="Angular navy and red header decoration"></div>

    <div class="brand">Wageline<br>Associates</div>

    <header class="holder">
      <h1 class="holder-name"><strong>NAME</strong> DAWSON</h1>
      <p class="holder-role">Purchase Manager</p>
    </header>

    <ul class="contacts">
      <li class="contact">
        <span class="contact-icon is-red"><svg viewBox="0 0 24 24"><path d="M12 3 2 12h3v8h5v-5h4v5h5v-8h3z"/></svg></span>
        <span class="contact-text">Street Address Here<br>Place, Near By, Post code</span>
      </li>
      <li class="contact">
        <span class="contact-icon is-navy"><svg viewBox="0 0 24 24"><path d="M2 11 22 3l-7 18-3-7z"/></svg></span>
        <span class="contact-text">hello@wageline.com</span>
      </li>
      <li class="contact">
        <span class="contact-icon is-red"><svg viewBox="0 0 24 24"><path d="M6.6 10.8a15 15 0 0 0 6.6 6.6l2.2-2.2c.3-.3.7-.4 1-.2 1.1.4 2.3.6 3.6.6.6 0 1 .4 1 1V20c0 .6-.4 1-1 1A17 17 0 0 1 3 4c0-.6.4-1 1-1h3.5c.6 0 1 .4 1 1 0 1.3.2 2.5.6 3.6.1.3 0 .7-.2 1z"/></svg></span>
        <span class="contact-text">+00 1480 2936 6158</span>
      </li>
      <li class="contact">
        <span class="contact-icon is-navy"><svg viewBox="0 0 24 24"><circle cx="12" cy="12" r="9" fill="none" stroke="#ffffff" stroke-width="2"/><path d="M3 12h18M12 3c3 3 3 15 0 18M12 3c-3 3-3 15 0 18" fill="none" stroke="#ffffff" stroke-width="1.6"/></svg></span>
        <span class="contact-text">www.wageline.com</span>
      </li>
    </ul>
  </article>
</body>
</html>
```